Business Card Design

I need a Business Card that will catch the attention that will not get thrown in a Drawer. I have 23 companies I use for Auto, Home, Life, and Business Insurance. I make sure that people have the best coverage for the $ spent.

Industry/Entity Type

Business

Contact Information for Business Card

Dorlin Insurance Agency, Inc., Marcus Helgren, 4375 West Tamber Lane Painesville, Westmarch 45192 555-281-7496, www.dorlinagency.example, Facelane, LinkedIn, Gloople+

```html
<!DOCTYPE html>
<html lang="en">
<head>
<meta charset="utf-8">
<title>Dorlin Insurance Agency — Business Card</title>
<link rel="stylesheet" href="https://fonts.googleapis.com/css2?family=Jost:wght@300;400;600&display=swap">
<style>
  :root {
    --page: #ffffff;
    --card-tint: #fdf5f3;
    --magenta: #c7386b;
    --coral: #d95a45;
    --red: #e0323a;
    --rule: #e88a78;
    --ink: #1e1e1e;
    --hex-fill-a: #f9ddd7;
    --hex-fill-b: #f4cdd9;
  }
  * { margin: 0; padding: 0; box-sizing: border-box; }
  html, body {
    width: 1200px; height: 899px; overflow: hidden;
    background: var(--page);
    font-family: "Jost", "Century Gothic", sans-serif;
  }
  .canvas { position: relative; width: 1200px; height: 899px; }
  .card-art { position: absolute; inset: 0; }
  .text { position: absolute; white-space: nowrap; color: var(--ink); font-weight: 300; line-height: 1; }
  .company-name { left: 430px; top: 237px; font-size: 38px; font-weight: 400; color: var(--red); letter-spacing: 1.4px; }
  .address { right: 252px; top: 294px; text-align: right; font-size: 27px; line-height: 36px; }
  .contact-label { right: 270px; top: 431px; font-size: 23px; font-weight: 600; color: var(--magenta); letter-spacing: 0.5px; }
  .phone-number { right: 252px; top: 466px; font-size: 28px; }
  .web-label { left: 600px; top: 503px; font-size: 22px; color: var(--red); }
  .web-address { left: 679px; top: 502px; font-size: 25px; }
  .follow-label { left: 544px; top: 629px; font-size: 22px; font-weight: 600; color: var(--magenta); letter-spacing: 0.8px; }
  .social-list { left: 682px; top: 628px; font-size: 24px; color: var(--magenta); }
</style>
</head>
<body>
<div class="canvas">
  <svg class="card-art" width="1200" height="899" viewBox="0 0 1200 899" xmlns="http://www.w3.org/2000/svg">
    <defs>
      <linearGradient id="band" x1="0" x2="1" y1="0" y2="0">
        <stop offset="0" stop-color="var(--magenta)"/>
        <stop offset="1" stop-color="var(--coral)"/>
      </linearGradient>
      <linearGradient id="hexFill" x1="0" x2="1" y1="0" y2="1">
        <stop offset="0" stop-color="var(--hex-fill-a)"/>
        <stop offset="1" stop-color="var(--hex-fill-b)"/>
      </linearGradient>
      <linearGradient id="hexEdge" x1="0" x2="1" y1="0" y2="1">
        <stop offset="0" stop-color="var(--coral)"/>
        <stop offset="1" stop-color="var(--magenta)"/>
      </linearGradient>
      <polygon id="hex" points="0,-57 54,-28.5 54,28.5 0,57 -54,28.5 -54,-28.5"/>
    </defs>

    <rect class="card-surface" x="92" y="138" width="971" height="570" fill="var(--card-tint)"/>

    <polygon class="band-top" points="382,138 1063,138 1063,194 438,194" fill="url(#band)"/>
    <polygon class="band-bottom" points="640,708 684,664 1063,664 1063,708" fill="url(#band)"/>

    <line class="hanger-line" x1="192" y1="138" x2="192" y2="253" stroke="var(--rule)" stroke-width="2.5"/>
    <line class="footer-rule" x1="419" y1="604" x2="1063" y2="604" stroke="var(--rule)" stroke-width="2.5"/>

    <circle cx="952" cy="259" r="4" fill="var(--coral)"/>
    <line x1="956" y1="259" x2="1063" y2="259" stroke="var(--rule)" stroke-width="1.8"/>
    <circle cx="954" cy="442" r="4" fill="var(--coral)"/>
    <line x1="958" y1="442" x2="1063" y2="442" stroke="var(--rule)" stroke-width="1.8"/>

    <g class="coverage-hexes" stroke="url(#hexEdge)" stroke-width="4" fill="url(#hexFill)">
      <use href="#hex" x="192" y="310" role="img" aria-label="Home insurance illustration"/>
      <use href="#hex" x="247" y="410" role="img" aria-label="Commercial building insurance illustration"/>
      <use href="#hex" x="192" y="506" role="img" aria-label="Construction crane illustration"/>
      <use href="#hex" x="247" y="610" role="img" aria-label="Life insurance family illustration"/>
      <use href="#hex" x="365" y="610" role="img" aria-label="Health coverage shield illustration"/>
    </g>

    <g class="phone-icon" fill="var(--red)">
      <path d="M612 485 q18 -13 36 0 v5 h-36 z"/>
      <rect x="614" y="488" width="32" height="4" rx="1"/>
    </g>
    <line class="contact-divider" x1="668" y1="466" x2="668" y2="492" stroke="var(--rule)" stroke-width="1.8"/>
    <line class="contact-divider" x1="668" y1="502" x2="668" y2="530" stroke="var(--rule)" stroke-width="1.8"/>
  </svg>

  <div class="text company-name">Dorlin Insurance Agency, Inc</div>
  <div class="text address">Marcus Helgren,<br>4375 West Tamber Lane Ashbrook<br>Westmarch 45192</div>
  <div class="text contact-label">Contact</div>
  <div class="text phone-number">555-281-7496</div>
  <div class="text web-label">www.</div>
  <div class="text web-address">www.dorlinagency.example</div>
  <div class="text follow-label">Follow Us</div>
  <div class="text social-list">Facelane | Linkpoint | Gloople+</div>
</div>
</body>
</html>
```